Brightgate Automotive Service Website Design

We are working with Brightgate Automotive Service. They are a local mechanic/garage and in need of a new website design.

Some sites to use for inspiration:

https://www.torvalle.example
https://www.quenby.example
https://parks-carcare.example
https://www.hollowmerefullautocare.example/

Thank you for taking the time to consider designing a website for us. We are web developers based in Stockton, CA, USA. Most of our projects go through the same process. Understanding this process may help you win a project with us. We custom-code all of our websites in-house. We don’t have any requirements as to what tools you use for your design, but we prefer Figma files. For any design that we label as four-stars, we send it to the client for review. The client picks the final design they want us to use. Once we complete this process, we will continue to show additional clients all the four-star sites and purchase them later. Your designs will have multiple chances to sell. For better chances of success, we ask that you follow these guidelines.

IMAGES:
If you use any images or icons in the design, we ask that you have a link to the asset so we can purchase the image/icon. Most of the designs we submit do not have the customer’s images on them unless they have some great images. Be creative; show us the feeling you are trying to portray with your image choices. Use any royalty-free site you choose. We subscribe to Adobe and mainly use their images, but we can purchase images outside of Adobe.

PLEASE NOTE: we will not submit designs to clients with watermarks on the images.

FONTS:
We ask that you identify the fonts used in the design. This can be done in a message if you want. We typically use Google Fonts and Adobe Fonts.

CONTENT:
We're always open to different content and ideas. We often submit designs with stock images so the client can see our vision. We typically take pictures after the website launch to use their images with our vision. Lorem Ipsum is fine for paragraphs, but we ask that you write the headers in correct English. We want to be able to show the vision and identify the sections of the website.

INSPIRATION:
We typically add a couple of links in the brief of websites we like to help you get started in your design.

REVISIONS:
We do not often ask for revisions of the designs unless we see something in the design that may not appeal to the client. If there are slight changes that we want to make, we do that in the development process.

FEEDBACK:
We rarely give feedback on designs during the design process. We are working on many website projects and do not have the time to provide feedback. We usually respond if your request is well thought out and asks specific questions, but a note asking “feedback, please” usually goes unanswered.

```html
<!DOCTYPE html>
<html lang="en">
<head>
<meta charset="utf-8">
<title>Brightgate Automotive Service</title>
<link rel="stylesheet" href="https://fonts.googleapis.com/css2?family=Bebas+Neue&family=Oswald:wght@500;600;700&family=Poppins:wght@500;600&family=Open+Sans:ital,wght@0,400;0,600;0,700;1,400&display=swap">
<style>
:root{
  --red:#c81c32;
  --red-soft:#c8404f;
  --red-deep:#b3141f;
  --pink:#fde9ec;
  --ink:#1c1c1c;
  --muted:#6d6d6d;
  --dark:#1e1e1e;
  --field:#eeeae8;
  --white:#ffffff;
}
*{box-sizing:border-box;margin:0;padding:0}
html,body{width:1200px;height:4787px;overflow:hidden}
body{position:relative;font-family:"Open Sans",sans-serif;color:var(--ink);background:var(--white)}
.abs{position:absolute}
.ph{position:absolute}
.btn{position:absolute;display:flex;align-items:center;justify-content:center;border-radius:20px;font-family:"Poppins",sans-serif;font-weight:600;font-size:16px}
.btn-solid{background:var(--red-soft);color:#fff}
.btn-line{border:2px solid var(--red-soft);color:var(--red-soft);background:transparent}
.h-cond{font-family:"Bebas Neue",sans-serif;font-weight:400;letter-spacing:.5px}

/* header */
.site-header{position:absolute;left:0;top:0;width:1200px;height:64px;background:#fff}
.brand{position:absolute;left:78px;top:14px;font-family:"Bebas Neue",sans-serif;font-size:40px;line-height:40px;color:#6a6a6a}
.nav{position:absolute;top:24px;left:344px;font-size:13px}
.nav a{color:var(--ink);text-decoration:none;position:absolute;white-space:nowrap}
.header-quote{left:908px;top:20px;width:100px;height:26px;font-size:12px}
.header-phone{position:absolute;left:1030px;top:23px;font-size:12px;font-weight:600;display:flex;gap:8px;align-items:center}

/* hero */
.hero{position:absolute;left:0;top:64px;width:1200px;height:593px;background:var(--pink)}
.hero-title{position:absolute;left:90px;top:126px;font-family:"Poppins",sans-serif;font-weight:600;font-size:50px;line-height:60px;color:var(--ink)}
.hero-text{position:absolute;left:90px;top:250px;width:440px;font-size:15px;line-height:18px;color:#444}

/* features */
.features{position:absolute;left:122px;top:561px;width:972px;height:254px;background:#fff;box-shadow:0 10px 30px rgba(0,0,0,.12)}
.feature{position:absolute;top:0;width:300px;text-align:center}
.feature .icon{margin:20px auto 0;width:90px;height:90px}
.feature h3{font-family:"Oswald",sans-serif;font-weight:600;font-size:20px;margin-top:12px;text-transform:uppercase}
.feature p{font-size:12px;line-height:16px;color:#555;margin:10px auto 0;width:232px}

/* who */
.who-title{left:620px;top:1010px;font-size:40px}
.who-text{left:620px;top:1070px;width:455px;font-size:13px;line-height:18px;color:#555}

/* services */
.services{position:absolute;left:0;top:1427px;width:1200px;height:905px;background:linear-gradient(135deg,#2a2a2a,#141414 60%,#222)}
.services-title{position:absolute;left:0;width:1200px;top:88px;text-align:center;color:#fff;font-size:42px}
.svc{position:absolute;width:241px;height:190px;background:#f6f6f6;border-radius:6px;text-align:center;box-shadow:0 8px 20px rgba(0,0,0,.4)}
.svc h3{font-family:"Open Sans",sans-serif;font-weight:700;font-size:15px;margin-top:60px;letter-spacing:.3px}
.svc p{font-size:10.5px;line-height:13px;color:#777;width:190px;margin:10px auto 0}
.svc-photo{position:absolute;width:100px;height:100px;border-radius:50%;left:70px;top:-62px;border:3px solid #fff}
.go{position:absolute;left:102px;bottom:-12px;width:32px;height:32px;border-radius:50%;background:var(--red);display:flex;align-items:center;justify-content:center}

/* quote */
.quote-title{left:96px;top:2522px;font-size:42px}
.quote-text{left:96px;top:2576px;width:420px;font-size:15px;line-height:18px;color:#444}
.field{position:absolute;height:38px;background:var(--field);border-radius:6px;font-size:12px;color:#b9b3b0;padding:11px 16px}
.submit{position:absolute;left:88px;top:2897px;width:623px;height:48px;border-radius:24px;background:var(--red-deep);color:#fff;font-size:15px;font-weight:600;display:flex;align-items:center;justify-content:center}
.quote-photo{left:752px;top:2480px;width:448px;height:565px;background:linear-gradient(180deg,#d9d9d9,#5a5a5a)}

/* testimonials */
.reviews{position:absolute;left:0;top:3045px;width:1200px;height:593px;background:var(--pink)}
.reviews-title{position:absolute;left:0;width:1170px;top:100px;text-align:center;font-size:42px}
.review{position:absolute;top:193px;width:238px;height:284px;background:#fff;text-align:center;box-shadow:0 6px 16px rgba(0,0,0,.06)}
.review .qm{position:absolute;left:12px;top:8px;color:var(--red);font-family:"Oswald",sans-serif;font-size:46px;line-height:46px;font-weight:700}
.avatar{width:76px;height:76px;border-radius:50%;margin:22px auto 0}
.review h4{font-family:"Oswald",serif;font-weight:500;font-size:12px;margin-top:16px;letter-spacing:.3px}
.review p{font-style:italic;font-size:11.5px;line-height:14px;color:#888;width:170px;margin:10px auto 0}
.stars{color:#c4c824;font-size:18px;margin-top:36px;letter-spacing:2px}

/* blog */
.blog-title{left:0;width:1175px;top:3725px;text-align:center;font-size:42px}
.post{position:absolute;top:3832px;width:264px;height:363px;background:#fff;box-shadow:0 6px 18px rgba(0,0,0,.1)}
.post-photo{position:absolute;left:0;top:0;width:264px;height:175px}
.tag{position:absolute;left:0;top:148px;background:#fff;color:var(--red);font-size:9px;padding:5px 12px 7px 14px}
.post h3{position:absolute;left:30px;top:200px;width:220px;font-family:"Oswald",sans-serif;font-weight:700;font-size:15px;line-height:25px;color:#213a72;text-transform:uppercase;letter-spacing:.5px}
.post p{position:absolute;left:30px;top:263px;width:210px;font-size:11px;line-height:18px;color:#888}
.post .more{position:absolute;left:30px;top:327px;font-family:"Oswald",sans-serif;font-size:9px;font-weight:700;color:var(--red);letter-spacing:.5px}

/* footer */
.site-footer{position:absolute;left:0;top:4335px;width:1200px;height:452px;background:linear-gradient(135deg,#262626,#151515)}
.foot-brand{position:absolute;left:98px;top:100px;font-family:"Bebas Neue",sans-serif;font-size:70px;line-height:70px;color:#8a8a8a}
.foot-about{position:absolute;left:96px;top:214px;width:270px;font-size:13px;line-height:17px;color:#fff}
.foot-col{position:absolute;top:118px;color:#fff}
.foot-col h4{font-family:"Bebas Neue",sans-serif;font-weight:400;font-size:27px;letter-spacing:.5px}
.foot-col ul{list-style:none;margin-top:18px}
.foot-col li{font-size:14px;line-height:32px;display:flex;align-items:center;gap:10px}
.foot-col li::before{content:"→";color:var(--red);font-size:14px}
.foot-col.hours li::before{content:none}
.foot-bottom{position:absolute;top:396px;color:#fff;font-size:12.5px}
</style>
</head>
<body>

<header class="site-header">
  <div class="brand">BRIGHTGATE</div>
  <nav class="nav">
    <a style="left:0">Home</a>
    <a style="left:83px">About</a>
    <a style="left:164px">Services</a>
    <a style="left:262px">Reviews</a>
    <a style="left:355px">Contact Us</a>
  </nav>
  <div class="btn btn-solid header-quote">Get a Quote</div>
  <div class="header-phone">
    <svg width="14" height="14" viewBox="0 0 24 24"><path fill="#c81c32" d="M6.6 10.8a15 15 0 0 0 6.6 6.6l2.2-2.2a1 1 0 0 1 1-.25 11.4 11.4 0 0 0 3.6.57 1 1 0 0 1 1 1V20a1 1 0 0 1-1 1A17 17 0 0 1 3 4a1 1 0 0 1 1-1h3.5a1 1 0 0 1 1 1c0 1.25.2 2.45.57 3.57a1 1 0 0 1-.25 1z"/></svg>
    123 456 7890
  </div>
</header>

<section class="hero">
  <svg class="abs" style="left:600px;top:0" width="600" height="593" viewBox="0 0 600 593">
    <polygon points="6,0 40,0 170,593 120,593 10,360 50,290" fill="#e0162d"/>
  </svg>
  <div class="ph" role="img" aria-label="Two mechanics in a workshop inspecting a car part, one holding a clipboard" style="left:660px;top:0;width:540px;height:593px;background:linear-gradient(120deg,#6f6f72,#2e2e33 55%,#8a3b3b);clip-path:polygon(0 0,100% 0,100% 100%,115px 100%,30px 355px,50px 290px)"></div>
  <h1 class="hero-title">We Are Qualified<br>and Professional</h1>
  <p class="hero-text">Lorem ipsum dolor sit amet, consectetur adipiscing elit, sed do eiusmod tempor incididunt ut labore et dolore magna aliqua. Ut enim ad minim veniam quis nostrud</p>
  <div class="btn btn-solid" style="left:89px;top:347px;width:140px;height:36px">Get a Quote</div>
  <div class="btn btn-line" style="left:241px;top:347px;width:150px;height:36px">123 456 7890</div>
</section>

<section class="features">
  <div class="feature" style="left:28px">
    <div class="icon" role="img" aria-label="Technician icon" style="border:3px solid var(--red);border-radius:50%"></div>
    <h3>Best Technicians</h3>
    <p>Lorem ipsum dolor sit amet, consectetur adipiscing elit, sed do eiusmod tempor incididunt ut labore et dolore magna aliqua.</p>
  </div>
  <div class="feature" style="left:334px">
    <div class="icon" role="img" aria-label="Quality badge with stars icon" style="border:3px solid var(--red);border-radius:50%"></div>
    <h3>Quality Services</h3>
    <p>Lorem ipsum dolor sit amet, consectetur adipiscing elit, sed do eiusmod tempor incididunt ut labore et dolore magna aliqua.</p>
  </div>
  <div class="feature" style="left:640px">
    <div class="icon" role="img" aria-label="Hand holding a coin icon" style="border:3px solid var(--red);border-radius:50%"></div>
    <h3>Affordable Prices</h3>
    <p>Lorem ipsum dolor sit amet, consectetur adipiscing elit, sed do eiusmod tempor incididunt ut labore et dolore magna aliqua.</p>
  </div>
</section>

<section class="who">
  <div class="ph" role="img" aria-label="Mechanic rolling a tyre" style="left:122px;top:925px;width:218px;height:348px;background:linear-gradient(160deg,#3d5a7e,#1c2634)"></div>
  <div class="ph" role="img" aria-label="Mechanic working under a car bonnet" style="left:357px;top:925px;width:203px;height:165px;background:linear-gradient(150deg,#4d6a8a,#2a2f36)"></div>
  <div class="ph" role="img" aria-label="Mechanic repairing an engine" style="left:357px;top:1110px;width:203px;height:163px;background:linear-gradient(150deg,#7a4a3c,#252a30)"></div>
  <h2 class="abs h-cond who-title">Who We Are</h2>
  <p class="abs who-text">Lorem ipsum dolor sit amet, consectetur adipiscing elit, sed do eiusmod tempor incididunt ut labore et dolore magna aliqua. Ut enim ad minim veniam, quis nostrud exercitation ullamco laboris nisi ut aliquip ex ea commodo consequat. Duis aute irure dolor in reprehenderit in voluptate velit esse</p>
  <div class="btn btn-solid" style="left:616px;top:1185px;width:138px;height:36px">Get a Quote</div>
</section>

<section class="services">
  <h2 class="h-cond services-title">What We Do</h2>

  <div class="svc" style="left:150px;top:273px">
    <div class="svc-photo ph" role="img" aria-label="Engine repair" style="background:linear-gradient(140deg,#4a6d90,#2b2e33)"></div>
    <h3>ENGINE REPAIR</h3><p>Lorem ipsum dolor sit amet, consecteturadipiscing do eiusmod tempor incididuntut labore et dolore Ut enim ad minim veniam quis nostrud</p>
    <div class="go"><svg width="12" height="12" viewBox="0 0 12 12"><path d="M4 2l4 4-4 4" stroke="#fff" stroke-width="2" fill="none"/></svg></div>
  </div>
  <div class="svc" style="left:478px;top:275px">
    <div class="svc-photo ph" role="img" aria-label="Oil change" style="background:linear-gradient(140deg,#a53a3a,#2b2e33)"></div>
    <h3>OIL CHANGE</h3><p>Lorem ipsum dolor sit amet, consecteturadipiscing do eiusmod tempor incididuntut labore et dolore Ut enim ad minim veniam quis nostrud</p>
    <div class="go"><svg width="12" height="12" viewBox="0 0 12 12"><path d="M4 2l4 4-4 4" stroke="#fff" stroke-width="2" fill="none"/></svg></div>
  </div>
  <div class="svc" style="left:804px;top:273px">
    <div class="svc-photo ph" role="img" aria-label="Brake repair" style="background:linear-gradient(140deg,#3c4f6e,#15181d)"></div>
    <h3>BRAKE REPAIR</h3><p>Lorem ipsum dolor sit amet, consecteturadipiscing do eiusmod tempor incididuntut labore et dolore Ut enim ad minim veniam quis nostrud</p>
    <div class="go"><svg width="12" height="12" viewBox="0 0 12 12"><path d="M4 2l4 4-4 4" stroke="#fff" stroke-width="2" fill="none"/></svg></div>
  </div>

  <div class="svc" style="left:150px;top:588px">
    <div class="svc-photo ph" role="img" aria-label="Electrical repair" style="background:linear-gradient(140deg,#7a3030,#23262b)"></div>
    <h3>ELECTRICAL REPAIR</h3><p>Lorem ipsum dolor sit amet, consecteturadipiscing do eiusmod tempor incididuntut labore et dolore Ut enim ad minim veniam quis nostrud</p>
    <div class="go"><svg width="12" height="12" viewBox="0 0 12 12"><path d="M4 2l4 4-4 4" stroke="#fff" stroke-width="2" fill="none"/></svg></div>
  </div>
  <div class="svc" style="left:478px;top:590px">
    <div class="svc-photo ph" role="img" aria-label="Car air conditioning vents" style="background:linear-gradient(140deg,#444,#0e0e0e)"></div>
    <h3>AC SERVICES</h3><p>Lorem ipsum dolor sit amet, consecteturadipiscing do eiusmod tempor incididuntut labore et dolore Ut enim ad minim veniam quis nostrud</p>
    <div class="go"><svg width="12" height="12" viewBox="0 0 12 12"><path d="M4 2l4 4-4 4" stroke="#fff" stroke-width="2" fill="none"/></svg></div>
  </div>
  <div class="svc" style="left:804px;top:588px">
    <div class="svc-photo ph" role="img" aria-label="Wheel and tyre change" style="background:linear-gradient(140deg,#6c8199,#23272d)"></div>
    <h3>WHEEL &amp; TIRES</h3><p>Lorem ipsum dolor sit amet, consecteturadipiscing do eiusmod tempor incididuntut labore et dolore Ut enim ad minim veniam quis nostrud</p>
    <div class="go"><svg width="12" height="12" viewBox="0 0 12 12"><path d="M4 2l4 4-4 4" stroke="#fff" stroke-width="2" fill="none"/></svg></div>
  </div>
</section>

<section class="quote">
  <h2 class="abs h-cond quote-title">Get A Quote</h2>
  <p class="abs quote-text">Lorem ipsum dolor sit amet, consectetur adipiscing elit, sed do eiusmod tempor incididunt ut labore et dolore magna aliqua. Ut enim ad minim veniam quis nostrud</p>
  <div class="field" style="left:418px;top:2633px;width:295px">Your Phone</div>
  <div class="field" style="left:91px;top:2676px;width:296px">Your Name</div>
  <div class="field" style="left:418px;top:2693px;width:295px">Select Service</div>
  <div class="field" style="left:91px;top:2737px;width:296px">Email Address</div>
  <div class="field" style="left:91px;top:2796px;width:622px;height:78px">Additional Message</div>
  <div class="submit">GET AN APPOINTMENT NOW</div>
  <div class="ph quote-photo" role="img" aria-label="Smiling mechanic in overalls holding a tyre and giving a thumbs up"></div>
</section>

<section class="reviews">
  <h2 class="h-cond reviews-title">What Client Say's</h2>
  <svg class="abs" style="left:108px;top:305px" width="18" height="30" viewBox="0 0 18 30"><path d="M15 2L3 15l12 13" stroke="#c81c32" stroke-width="3" fill="none"/></svg>
  <svg class="abs" style="left:1043px;top:305px" width="18" height="30" viewBox="0 0 18 30"><path d="M3 2l12 13L3 28" stroke="#c81c32" stroke-width="3" fill="none"/></svg>

  <div class="review" style="left:193px">
    <div class="qm">“</div>
    <div class="avatar ph" role="img" aria-label="Client portrait" style="position:relative;background:linear-gradient(140deg,#c9a58e,#6d5a50)"></div>
    <h4>OWEN HARTLEY</h4>
    <p>Lorem ipsum dolor sit amet, consectetuer adipiscing elit, sed diam nonummy nibh euismod tincidunt ut laoreet dolore magna aliquam</p>
    <div class="stars">★★★★★</div>
  </div>
  <div class="review" style="left:470px">
    <div class="qm">“</div>
    <div class="avatar ph" role="img" aria-label="Client portrait" style="position:relative;background:linear-gradient(140deg,#6b4a3a,#1d1a1a)"></div>
    <h4>DJ CARVER</h4>
    <p>Lorem ipsum dolor sit amet, consectetuer adipiscing elit, sed diam nonummy nibh euismod tincidunt ut laoreet dolore magna aliquam</p>
    <div class="stars">★★★★★</div>
  </div>
  <div class="review" style="left:745px">
    <div class="qm">“</div>
    <div class="avatar ph" role="img" aria-label="Client portrait" style="position:relative;background:linear-gradient(140deg,#8a4a3a,#3a1f1a)"></div>
    <h4>LENA R MORROW</h4>
    <p>Lorem ipsum dolor sit amet, consectetuer adipiscing elit, sed diam nonummy nibh euismod tincidunt ut laoreet dolore magna aliquam</p>
    <div class="stars">★★★★★</div>
  </div>
</section>

<section class="blog">
  <h2 class="abs h-cond blog-title">Latest From Blog</h2>
  <article class="post" style="left:163px">
    <div class="post-photo ph" role="img" aria-label="Mechanic working on an engine in a garage" style="background:linear-gradient(150deg,#3f5676,#1f232a)"></div>
    <span class="tag">Maintenance</span>
    <h3>How Often Should You Detail Your Car</h3>
    <p>Lorem ipsum dolor sit amet, consectetur adipiscing elit, sed do eiusmod tempor incididunt ut...</p>
    <span class="more">READ MORE →</span>
  </article>
  <article class="post" style="left:449px">
    <div class="post-photo ph" role="img" aria-label="Mechanic inspecting a car underbody" style="background:linear-gradient(150deg,#5a7aa0,#22262d)"></div>
    <span class="tag">Engine Care</span>
    <h3>Detailing Your Car For Special Occasions</h3>
    <p>Lorem ipsum dolor sit amet, consectetur adipiscing elit, sed do eiusmod tempor incididunt ut...</p>
    <span class="more">READ MORE →</span>
  </article>
  <article class="post" style="left:735px">
    <div class="post-photo ph" role="img" aria-label="Mechanic repairing a car on a lift" style="background:linear-gradient(150deg,#33507a,#161a22)"></div>
    <span class="tag">Engine Care</span>
    <h3>The Power Of A Proper Tune Up On Car</h3>
    <p>Lorem ipsum dolor sit amet, consectetur adipiscing elit, sed do eiusmod tempor incididunt ut...</p>
    <span class="more">READ MORE →</span>
  </article>
</section>

<footer class="site-footer">
  <div class="foot-brand">BRIGHTGATE</div>
  <p class="foot-about">Lorem ipsum dolor sit amet, consectetur adipiscing elit, sed do eiusmod tempor.</p>
  <div class="foot-col" style="left:400px">
    <h4>Quick Links</h4>
    <ul><li>HOME</li><li>ABOUT</li><li>SERVICES</li><li>TESTIMONIALS</li><li>CONTACT US</li></ul>
  </div>
  <div class="foot-col" style="left:596px">
    <h4>Our Services</h4>
    <ul><li>TECHNICAL REPAIRD</li><li>OIL &amp; FILTERS</li><li>TIRES AND WHEELS</li><li>ELECTRICAL SYSTEMS</li><li>ENGINES REPAIRS</li></ul>
  </div>
  <div class="foot-col hours" style="left:857px">
    <h4>Opening Hours</h4>
    <ul><li>MONDAY – FRIDAY , 8 AM – 7 PM</li><li>SATURDAY, CLOSED</li><li>SUNDAY, CLOSED</li></ul>
  </div>
  <div class="foot-bottom" style="left:102px">Car Repair &amp; Auto Service</div>
  <div class="foot-bottom" style="left:898px">Privacy Policy- Terms &amp; Conditions</div>
</footer>

</body>
</html>
```